All-natural soap packaging design for new company

The box type has been selected, we just need artwork for each of our 10 products. I'd like the same look to each, the idea is just to switch out the name and ingredient label on each. The dimensions are 3.5"x3.75"x1.25". The colors in the uploaded pictures with product titles are not mandatory. I'd like to keep the font on the packaging (Rubik) as it is the same as the website.

Target Market(s)

Health & Beauty, people looking for natural or organic products

Industry/Entity Type

It Company

Colors

Designer to choose colors to be used in the design.

Requirements
Must have
• Design must be clean and relatively simple. Slightly different look for each of the 10 products. Audience is people looking for all-natural products.

```html
<!DOCTYPE html>
<html lang="en">
<head>
<meta charset="utf-8">
<title>Handmade Soap – Lavender Witch Hazel</title>
<link href="https://fonts.googleapis.com/css2?family=Rubik:wght@300;400;500&display=swap" rel="stylesheet">
<style>
  :root {
    --page: #ffffff;
    --brand-blue: #0b72ba;
    --ink: #1d1d1f;
    --frame: #222222;
    --marble-light: #f7f7f7;
    --marble-vein: #d9d9d9;
    --lavender-deep: #7a5fb0;
    --lavender-soft: #b9a6dd;
    --stem-green: #8ca66a;
  }
  html, body {
    margin: 0;
    width: 1200px;
    height: 880px;
    overflow: hidden;
    background: var(--page);
  }
  .canvas {
    position: relative;
    width: 1200px;
    height: 880px;
  }
  .soap-label {
    position: absolute;
    left: 312px;
    top: 194px;
    width: 579px;
    height: 494px;
    border: 1px solid var(--frame);
    box-sizing: border-box;
    overflow: hidden;
  }
  .marble-background {
    position: absolute;
    inset: 0;
    background:
      linear-gradient(160deg, transparent 30%, var(--marble-vein) 34%, transparent 40%),
      linear-gradient(20deg, transparent 55%, var(--marble-vein) 60%, transparent 66%),
      radial-gradient(ellipse at 20% 25%, #e6e6e6 0%, transparent 45%),
      radial-gradient(ellipse at 85% 70%, #e8e8e8 0%, transparent 45%),
      var(--marble-light);
  }
  .label-art {
    position: absolute;
    inset: 0;
    font-family: 'Rubik', sans-serif;
  }
  .tagline { font-weight: 300; font-size: 24px; fill: var(--ink); }
  .product-title { font-weight: 400; font-size: 48px; fill: var(--ink); }
  .scent-name { font-weight: 400; font-size: 15px; fill: var(--ink); letter-spacing: 0.3px; }
  .brand-name { font-weight: 500; font-size: 9px; fill: #555555; }
</style>
</head>
<body>
<div class="canvas">
  <div class="soap-label">
    <div class="marble-background" role="img" aria-label="White marble texture with soft grey veins"></div>
    <svg class="label-art" width="577" height="492" viewBox="0 0 577 492" xmlns="http://www.w3.org/2000/svg">
      <defs>
        <clipPath id="top-band-clip"><rect x="129" y="0" width="324" height="167"/></clipPath>
        <linearGradient id="lavender-fill" x1="0" y1="0" x2="1" y2="1">
          <stop offset="0" stop-color="var(--lavender-soft)"/>
          <stop offset="0.55" stop-color="var(--lavender-deep)"/>
          <stop offset="1" stop-color="var(--stem-green)"/>
        </linearGradient>
      </defs>

      <g class="top-band">
        <rect x="129" y="0" width="324" height="167" fill="var(--brand-blue)"/>
        <polyline points="137,0 137,159 445,159 445,0" fill="none" stroke="#ffffff" stroke-width="2"/>
        <g clip-path="url(#top-band-clip)">
          <ellipse cx="290" cy="128" rx="61" ry="100" fill="#ffffff"/>
        </g>
        <rect class="brand-mark" x="274" y="80" width="32" height="32" fill="var(--brand-blue)"/>
        <text class="brand-name" x="290" y="140" text-anchor="middle">ALDER SOAP CO.</text>
      </g>

      <text class="tagline" x="290" y="220" text-anchor="middle">100% NATURAL</text>
      <text class="product-title" x="290" y="268" text-anchor="middle">HANDMADE SOAP</text>
      <text class="scent-name" x="290" y="300" text-anchor="middle" xml:space="preserve">LAVENDER   WITCH HAZEL</text>

      <g class="bottom-band">
        <rect x="129" y="332" width="324" height="162" fill="var(--brand-blue)"/>
        <polyline points="137,494 137,340 445,340 445,494" fill="none" stroke="#ffffff" stroke-width="2"/>
        <ellipse cx="290" cy="409" rx="80" ry="52" fill="#ffffff"/>
        <ellipse cx="290" cy="409" rx="62" ry="30" fill="url(#lavender-fill)" role="img" aria-label="Photo of a bundle of fresh lavender sprigs"/>
      </g>
    </svg>
  </div>
</div>
</body>
</html>
```